Business Cards and Letter Head for Mini Excavator Hire Business
Business Cards and Letter Heads
Stone-Willow
Dermot Halvey
Mini Excavator Specialist
41 Morlena Court
Kelverton Vic 3208
dermot@plovtrek.com.au
plovtrek.com.au
Would like the front and back of the business card to be black (C:75 M:68 K:90).
Font: Helvetica CondensedBlack
• BRX Mini Hydraulic Excavator Hire
• From $297.00 per day including GST
• Cheaper rates for weekly or monthly hire
• Supplied complete with trailer & 3 buckets
• Auger attachments available
Book yours today!
Information regarding the business card design.
Logo design attached.

```html
<!DOCTYPE html>
<html lang="en">
<head>
<meta charset="utf-8">
<title>Plovtrek Hire – Business Card</title>
<link rel="stylesheet" href="https://fonts.googleapis.com/css2?family=Oswald:wght@700&family=Michroma&display=swap">
<style>
  :root {
    --page: #d9d6d1;
    --card: #1f1f1e;
    --yellow: #f4d21c;
    --white: #f2f2f0;
    --muted: #c9c9c4;
  }
  * { box-sizing: border-box; margin: 0; padding: 0; }
  html, body {
    width: 1200px; height: 900px; overflow: hidden;
    background: var(--page);
  }
  .canvas {
    width: 1200px; height: 900px;
    display: flex; align-items: center; justify-content: center;
  }
  .business-card {
    position: relative;
    width: 1000px; height: 612px;
    background: var(--card);
    border-radius: 4px;
    font-family: "Michroma", sans-serif;
    color: var(--muted);
  }
  .brand {
    position: absolute; top: 150px; left: 0; right: 0;
    display: flex; flex-direction: column; align-items: center;
  }
  .brand-row { display: flex; align-items: center; gap: 20px; }
  .brand-square { width: 70px; height: 70px; background: var(--yellow); }
  .brand-name {
    font-family: "Oswald", sans-serif; font-weight: 700;
    font-size: 78px; line-height: 1; letter-spacing: 1px;
    color: var(--yellow); text-transform: uppercase;
  }
  .brand-tagline {
    margin-top: 10px; margin-left: 90px;
    font-family: "Oswald", sans-serif; font-weight: 700;
    font-size: 22px; color: var(--white);
  }
  .holder {
    position: absolute; top: 360px; left: 0; right: 0;
    text-align: center; font-size: 14px; letter-spacing: 2px;
  }
  .holder-name { color: var(--yellow); }
  .holder-divider { color: var(--muted); margin: 0 10px; }
  .contacts {
    position: absolute; right: 40px; font-size: 13px; letter-spacing: 1px;
    display: flex; gap: 26px; align-items: center;
  }
  .contacts-address { top: 470px; }
  .contacts-phone { top: 512px; }
  .contact { display: flex; align-items: center; gap: 9px; white-space: nowrap; }
  .contact-icon { width: 18px; height: 18px; flex: none; }
</style>
</head>
<body>
<main class="canvas">
  <section class="business-card" aria-label="Plovtrek Hire business card">
    <header class="brand">
      <div class="brand-row">
        <span class="brand-square" aria-hidden="true"></span>
        <span class="brand-name">Plovtrek Hire</span>
      </div>
      <p class="brand-tagline">Dig deeper and pay less</p>
    </header>

    <p class="holder">
      <span class="holder-name">Dermot Halvey</span><span class="holder-divider">|</span><span class="holder-role">Mini Excavator Specialist</span>
    </p>

    <div class="contacts contacts-address">
      <span class="contact">
        <svg class="contact-icon" viewBox="0 0 18 18" aria-hidden="true"><circle cx="9" cy="9" r="9" fill="var(--yellow)"/><path d="M9 3.5a3.6 3.6 0 0 0-3.6 3.6C5.4 10 9 14.5 9 14.5s3.6-4.5 3.6-7.4A3.6 3.6 0 0 0 9 3.5zm0 5a1.4 1.4 0 1 1 0-2.8 1.4 1.4 0 0 1 0 2.8z" fill="var(--card)"/></svg>
        41 Morlena Court Kelverton Vic 3208
      </span>
      <span class="contact">
        <svg class="contact-icon" viewBox="0 0 18 18" aria-hidden="true"><circle cx="9" cy="9" r="9" fill="var(--yellow)"/><g fill="none" stroke="var(--card)" stroke-width="1.2"><circle cx="9" cy="9" r="5"/><ellipse cx="9" cy="9" rx="2.2" ry="5"/><path d="M4 9h10"/></g></svg>
        www.plovtrek.com.au
      </span>
    </div>

    <div class="contacts contacts-phone">
      <span class="contact">
        <svg class="contact-icon" viewBox="0 0 18 18" aria-hidden="true"><circle cx="9" cy="9" r="9" fill="var(--yellow)"/><path d="M6.2 4.5l1.6 2-1 1.2a6 6 0 0 0 3.5 3.5l1.2-1 2 1.6-1 1.7c-3.8-.2-7.1-3.5-7.3-7.3z" fill="var(--card)"/></svg>
        1-300-472-918
      </span>
      <span class="contact">
        <svg class="contact-icon" viewBox="0 0 18 18" aria-hidden="true"><circle cx="9" cy="9" r="9" fill="var(--yellow)"/><rect x="6" y="3.8" width="6" height="10.4" rx="1" fill="var(--card)"/><rect x="7" y="5" width="4" height="6.5" fill="var(--yellow)"/></svg>
        041-285-736-4
      </span>
      <span class="contact">
        <svg class="contact-icon" viewBox="0 0 18 18" aria-hidden="true"><circle cx="9" cy="9" r="9" fill="var(--yellow)"/><path d="M6.2 4.5l1.6 2-1 1.2a6 6 0 0 0 3.5 3.5l1.2-1 2 1.6-1 1.7c-3.8-.2-7.1-3.5-7.3-7.3z" fill="var(--card)"/></svg>
        039-517-204-6
      </span>
      <span class="contact">
        <svg class="contact-icon" viewBox="0 0 18 18" aria-hidden="true"><circle cx="9" cy="9" r="9" fill="var(--yellow)"/><rect x="4.5" y="5.8" width="9" height="6.4" fill="var(--card)"/><path d="M4.8 6.2L9 9.4l4.2-3.2" fill="none" stroke="var(--yellow)" stroke-width="1"/></svg>
        dermot@plovtrek.com.au
      </span>
    </div>
  </section>
</main>
</body>
</html>
```